Business Card Design Project

Financial planning, Insurance and Real estate - Financial Services company

Contact Information for Business Card

Looking for something simple in design -
Tolverin Equity LLC
Tolverin Wealth Managment

```html
<!DOCTYPE html>
<html lang="en">
<head>
<meta charset="utf-8">
<title>Tolverin Wealth Management – Business Card</title>
<link rel="stylesheet" href="https://fonts.googleapis.com/css2?family=Open+Sans:wght@400;600;700;800&display=swap">
<style>
  :root {
    --brand-blue: #1e7fc7;
    --brand-blue-deep: #1668a8;
    --ink: #1c1c1c;
    --paper: #ffffff;
    --card-black: #111214;
    --backdrop: #e7e9ec;
  }
  * { margin: 0; padding: 0; box-sizing: border-box; }
  html, body {
    width: 1200px;
    height: 900px;
    overflow: hidden;
    background: var(--backdrop);
    font-family: "Open Sans", sans-serif;
  }
  .canvas {
    position: relative;
    width: 1200px;
    height: 900px;
    display: flex;
    align-items: center;
    justify-content: center;
    gap: 36px;
  }
  .card {
    position: relative;
    width: 520px;
    height: 300px;
    border-radius: 22px;
    overflow: hidden;
    box-shadow: 0 10px 30px rgba(0,0,0,0.18);
    flex: none;
  }

  /* Front */
  .card-front { background: var(--paper); }
  .card-front .top-band {
    position: absolute; left: 0; top: 0; right: 0;
    height: 12px; background: var(--brand-blue);
  }
  .card-front .bottom-band {
    position: absolute; left: 0; right: 0; bottom: 0;
    height: 40px; background: var(--brand-blue);
    display: flex; align-items: center;
    padding-left: 24px;
  }
  .tagline {
    color: var(--paper);
    font-size: 13.5px;
    font-weight: 400;
    white-space: nowrap;
  }
  .identity {
    position: absolute; left: 24px; top: 32px;
  }
  .person-name {
    color: var(--brand-blue);
    font-size: 22px;
    font-weight: 700;
    letter-spacing: 0.5px;
    line-height: 1.1;
  }
  .person-role {
    color: var(--ink);
    font-size: 13px;
    font-weight: 800;
    letter-spacing: 0.3px;
  }
  .contact-list {
    position: absolute; left: 24px; top: 104px;
    list-style: none;
  }
  .contact-list li {
    display: flex; align-items: center; gap: 8px;
    color: var(--ink);
    font-size: 14px;
    line-height: 23px;
    white-space: nowrap;
  }
  .contact-list svg { width: 13px; height: 13px; fill: var(--brand-blue); flex: none; }
  .brand-lockup {
    display: flex; align-items: center; gap: 10px;
  }
  .card-front .brand-lockup {
    position: absolute; right: 28px; bottom: 56px;
  }
  .brand-dot {
    width: 22px; height: 22px; border-radius: 50%;
    background: var(--brand-blue);
    flex: none;
  }
  .brand-name {
    color: var(--brand-blue);
    font-size: 17px;
    font-weight: 700;
    white-space: nowrap;
  }

  /* Back */
  .card-back {
    background: var(--card-black);
    display: flex; align-items: center; justify-content: center;
  }
  .card-back .brand-name { font-size: 20px; }
  .card-back .brand-dot { width: 26px; height: 26px; }
</style>
</head>
<body>
  <main class="canvas">
    <section class="card card-front" aria-label="Business card front">
      <div class="top-band"></div>
      <div class="identity">
        <h1 class="person-name">JOHNATHAN DOE</h1>
        <p class="person-role">MANAGER</p>
      </div>
      <ul class="contact-list">
        <li>
          <svg viewBox="0 0 24 24" aria-hidden="true"><path d="M6.6 10.8a15.1 15.1 0 0 0 6.6 6.6l2.2-2.2c.3-.3.7-.4 1-.2 1.1.4 2.3.6 3.6.6.6 0 1 .4 1 1V20c0 .6-.4 1-1 1A17 17 0 0 1 3 4c0-.6.4-1 1-1h3.5c.6 0 1 .4 1 1 0 1.3.2 2.5.6 3.6.1.3 0 .7-.2 1z"/></svg>
          01 234 567
        </li>
        <li>
          <svg viewBox="0 0 24 24" aria-hidden="true"><path d="M2 5h20v14H2z M4 7v.5l8 5 8-5V7l-8 5z" fill-rule="evenodd"/></svg>
          email@domainname.com
        </li>
        <li>
          <svg viewBox="0 0 24 24" aria-hidden="true"><path d="M12 2a10 10 0 1 0 0 20 10 10 0 0 0 0-20zm6.9 6h-3a15.7 15.7 0 0 0-1.4-3.6A8 8 0 0 1 18.9 8zM12 4c.8 1.2 1.5 2.5 1.9 4h-3.8c.4-1.5 1.1-2.8 1.900-4zM4.3 14a8 8 0 0 1 0-4h3.4a16.5 16.5 0 0 0 0 4zm.8 2h3a15.7 15.7 0 0 0 1.4 3.6A8 8 0 0 1 5.1 16zm3-8h-3a8 8 0 0 1 4.4-3.6C8.9 5.5 8.4 6.7 8.1 8zM12 20c-.8-1.2-1.5-2.5-1.9-4h3.8c-.4 1.5-1.1 2.8-1.9 4zm2.3-6H9.7a14.7 14.7 0 0 1 0-4h4.6a14.7 14.7 0 0 1 0 4zm.3 5.6c.6-1.1 1.1-2.3 1.4-3.6h3a8 8 0 0 1-4.4 3.6zm1.7-5.6a16.5 16.5 0 0 0 0-4h3.4a8 8 0 0 1 0 4z"/></svg>
          www.WebsiteGoesHere.com
        </li>
      </ul>
      <div class="brand-lockup">
        <span class="brand-dot" aria-hidden="true"></span>
        <span class="brand-name">Tolverin Wealth Management</span>
      </div>
      <div class="bottom-band">
        <p class="tagline">Financial planning Insurance and Real estate - Financial Services company</p>
      </div>
    </section>

    <section class="card card-back" aria-label="Business card back">
      <div class="brand-lockup">
        <span class="brand-dot" aria-hidden="true"></span>
        <span class="brand-name">Tolverin Wealth Management</span>
      </div>
    </section>
  </main>
</body>
</html>
```